Vellmont Archive Systems Quillbase 720 Flyer

We have a requirement to start sending out product / service information to our clients and resellers. Currently this type of communication is only via the LinkedIn/ Twitter / Blog articles and we want to change this to an email campaign with pdf and the ability to print and send by post.

We have a powerpoint draft of the flyer that will be a pdf and potentially a handout but it looks like a powerpoint and not something classy. I have included the powerpoint and four images along with our current logo (although this may change soon)

Target Market(s)

MSP Resellers, Direct Clients

Industry/Entity Type

It Service

Colors

Designer to choose colors to be used in the design.

Requirements
Must have
• The flow and feel from our website and social media so that it has our identity. Our core colors are on the website. Anything new must be complementary.
• Modern and technical feel
Nice to have
• Sense of security and trust. Our new strap line is to be "Simple, Safe, Secure" so some experimentation on this would be nice
Should not have
• nothing of note

```html
<!DOCTYPE html>
<html lang="en">
<head>
<meta charset="utf-8">
<title>Vellmont Archive Systems – Know the Facts</title>
<link href="https://fonts.googleapis.com/css2?family=Open+Sans:wght@300;400;700&display=swap" rel="stylesheet">
<style>
  :root {
    --paper: #ffffff;
    --ink: #7a7a7a;
    --ink-strong: #6a6a6a;
    --headline: #c3c5ae;
    --eyebrow: #8a8a8a;
    --photo-wall: #c8ceb7;
    --photo-wall-light: #d3d8c3;
    --photo-desk: #2f3238;
    --brand: #3a3f44;
    --brand-dot: #3f8fcf;
  }
  * { margin: 0; padding: 0; box-sizing: border-box; }
  html, body { width: 855px; height: 1200px; overflow: hidden; background: var(--paper); }
  body { font-family: "Open Sans", Arial, sans-serif; }
  .flyer { position: relative; width: 855px; height: 1200px; background: var(--paper); }

  .eyebrow {
    position: absolute; top: 30px; right: 33px;
    font-weight: 300; font-size: 17.5px; letter-spacing: 0.4px;
    color: var(--eyebrow); text-transform: uppercase;
  }
  .headline {
    position: absolute; left: 140px; top: 88px;
    font-weight: 300; font-size: 74px; line-height: 80px; letter-spacing: -1px;
    color: var(--headline); text-transform: uppercase; white-space: nowrap;
  }
  .hero {
    position: absolute; left: 143px; top: 154px; width: 712px; height: 475px;
    background:
      linear-gradient(to bottom, transparent 0, transparent 88%, var(--photo-desk) 88%, #1f2226 100%),
      radial-gradient(ellipse at 50% 35%, var(--photo-wall-light), var(--photo-wall) 70%);
  }
  .body-copy {
    position: absolute; left: 143px; top: 664px; width: 660px;
    font-size: 17px; line-height: 20px; color: var(--ink);
  }
  .body-copy p { margin-bottom: 20px; }
  .body-copy .lead-in { font-weight: 700; color: var(--ink-strong); margin-bottom: 20px; }
  .body-copy strong { font-weight: 700; color: var(--ink-strong); }

  .brand {
    position: absolute; left: 40px; top: 1140px;
    display: flex; align-items: center; gap: 12px;
  }
  .brand-dot { width: 26px; height: 26px; border-radius: 50%; background: var(--brand-dot); }
  .brand-name {
    font-weight: 400; font-size: 19px; letter-spacing: -0.2px;
    color: var(--brand); text-transform: uppercase;
  }
</style>
</head>
<body>
<main class="flyer">
  <div class="eyebrow">The reasons why you need to backup Quillbase 720</div>
  <h1 class="headline">Know the facts</h1>

  <div class="hero" role="img" aria-label="Photograph of a young inventor in a suit and goggles wearing a homemade colander helmet with wires, seated at a desk beside an old meter, writing in a notebook against a pale sage wall"></div>

  <section class="body-copy">
    <p>Halvorsen Quillbase 720 is quickly becoming the “go to” for businesses and the adoption of this shows no signs of slowing down anytime soon. There is no doubting that the services that they provide are robust and the uptime statistics certainly demonstrate that they are focused on providing a solid infrastructure for their services.</p>
    <p class="lead-in">So, nothing to worry about then ?</p>
    <p>Wrong, unfortunately, there is a common misconception that this service also provides backups of your data. In fact the responsibility of this remains with you.</p>
    <p>The reality is that without backups, you are left open to data loss and reports state that 1 in 3 businesses that have adopted cloud technology have experienced this. Without a change in the mindset, you are increasing risk and could lead to damaging repercussions for your business.</p>
    <p>You need to <strong>take control of your data</strong> and introduce a cloud backup solution that takes care of the day to day backups of your Quillbase 720, provides you with data protection and a retention policy that suits your business requirements</p>
  </section>

  <footer class="brand">
    <span class="brand-dot"></span>
    <span class="brand-name">Vellmont Archive Systems</span>
  </footer>
</main>
</body>
</html>
```